Wellness Thai Massage Geschäft benötigt eine Preis/Info Broschüre

Ein kleines Thai Massage Geschäft in Bayern: Sukonta Thaimassage
Benötigt eine kleine Preisliste, sowie eine kurze Beschreibung vom Unternehmen. Angeboten werden traditionelle Thaimassagen. Der Farbstil soll dem Logo (Anhang) angepasst sein. Alle Bilder außer die Bilder von der Geschäftsführerin sind optional zur Verwendung verfügbar. Mehr Info wie Preise, etc. sind verfügbar auf der Website https://www.sukontathaimassage-beispiel.de/

```html
<!DOCTYPE html>
<html lang="de">
<head>
<meta charset="utf-8">
<title>Sukonta Thaimassage – Broschüre</title>
<link href="https://fonts.googleapis.com/css2?family=Cinzel:wght@400;700&family=Dancing+Script:wght@500&family=Roboto+Condensed:ital,wght@0,400;0,700;1,400;1,700&family=Roboto:ital,wght@1,400;1,700&display=swap" rel="stylesheet">
<style>
:root{
  --bg:#cfcfcf;
  --cream:#fdf6cc;
  --cream-2:#fbeec0;
  --paper:#f7f1ec;
  --wine:#8a1a1e;
  --wine-dark:#6f1216;
  --raspberry:#d3204f;
  --rose:#e7a3c4;
  --orange:#e59a1e;
  --text:#3a2a22;
}
*{box-sizing:border-box;margin:0;padding:0}
html,body{width:1018px;height:1200px;overflow:hidden}
body{background:var(--bg);font-family:"Roboto Condensed",sans-serif;color:var(--text);position:relative}

.spread{position:absolute;left:147px;width:678px;overflow:hidden}
.spread--cover{top:91px;height:480px;background:linear-gradient(90deg,var(--cream) 0 50%,#fcefc6 50% 100%)}
.spread--inside{top:644px;height:478px;background:linear-gradient(90deg,#f6eee8 0 50%,#fbf8f6 50% 100%)}
.spread svg.waves{position:absolute;inset:0;width:100%;height:100%}
.abs{position:absolute}

/* brand mark */
.brand{position:absolute;display:flex;align-items:center;gap:8px;z-index:2}
.brand__dot{width:30px;height:30px;border-radius:50%;background:var(--rose)}
.brand__name{font-family:"Roboto Condensed",sans-serif;font-weight:700;color:var(--wine);font-size:17px;line-height:1.05;text-transform:uppercase;letter-spacing:1px}

/* cover left */
.photo-circle{position:absolute;border-radius:50%;border:3px solid #fff}
.contact__title{left:0;width:339px;top:268px;text-align:center;font-family:"Cinzel",serif;font-size:22px;color:var(--wine);letter-spacing:1px}
.contact__sub{left:0;width:339px;top:293px;text-align:center;font-style:italic;font-weight:700;font-size:12.5px;color:var(--wine)}
.rule{position:absolute;height:1px;background:var(--wine)}
.address{left:26px;top:326px;color:var(--wine);font-size:12px;line-height:15px}
.address .phone{font-weight:700;font-size:18px;line-height:22px;display:block;margin-top:2px}
.address .mail{font-size:10.5px;display:block}
.hours{left:182px;top:326px;color:var(--wine);font-size:10px;line-height:12.6px}
.hours strong{font-weight:700}
.divider-v{left:166px;top:330px;width:1px;height:60px;background:var(--wine)}
.booking__label{left:0;width:339px;top:398px;text-align:center;font-weight:700;font-size:10px;color:var(--wine);letter-spacing:.3px}
.booking__text{left:0;width:339px;top:411px;text-align:center;font-style:italic;font-size:10px;line-height:13px;color:var(--wine)}
.web-pill{left:64px;top:443px;width:204px;height:19px;border-radius:10px;background:var(--raspberry);color:#fff;font-size:12px;line-height:19px;text-align:center;white-space:nowrap}

/* cover right */
.welcome{left:339px;width:339px;top:338px;text-align:center;font-family:"Cinzel",serif;font-size:30px;color:var(--wine);letter-spacing:1px}
.welcome__script{left:339px;width:339px;top:371px;text-align:center;font-family:"Dancing Script",cursive;font-size:20px;color:var(--raspberry)}
.welcome__text{left:339px;width:339px;top:403px;text-align:center;font-family:"Roboto",sans-serif;font-style:italic;font-size:10px;line-height:12.5px;color:#2a1a16}
.welcome__phone{left:339px;width:339px;top:432px;text-align:center;font-weight:700;font-size:20px;color:var(--wine)}
.welcome__social{left:339px;width:339px;top:459px;text-align:center;font-size:8px;color:var(--wine);letter-spacing:.5px}

/* inside left */
.photo{position:absolute}
.section-title{position:absolute;left:129px;width:189px;height:14px;background:linear-gradient(90deg,#f6ebb2,#faf2c9);display:flex;align-items:center;gap:5px;font-weight:700;color:var(--wine);font-size:12px;padding-left:3px}
.section-title::before{content:"";width:9px;height:9px;border-radius:50%;background:var(--rose)}
.copy{position:absolute;left:129px;width:189px;font-size:8px;line-height:10.6px;text-align:justify;color:#2a1d18}

.price{position:absolute;left:23px;top:254px;width:295px;border-collapse:collapse;font-size:9px}
.price th{background:var(--wine);color:#fff;font-weight:700;height:22px;text-align:left;padding-left:10px;font-size:9.5px}
.price th.num{text-align:center;padding:0}
.price td{border-top:1px solid var(--wine);background:#fbf1c4;color:var(--wine);line-height:10px}
.price td.name{font-weight:700;padding-left:9px;font-size:9.5px;border-left:1px solid var(--wine)}
.price td.min{text-align:center;border-left:1px solid var(--wine);color:#5a3a30}
.price td.eur{text-align:center;background:var(--wine);color:#fbe8c4}
.price tr:last-child td{border-bottom:1px solid var(--wine)}

/* inside right */
.service{position:absolute;left:444px;width:216px}
.service h3{font-size:11.5px;font-weight:700;color:var(--wine);border-bottom:1px solid #c99;padding-bottom:1px;margin-bottom:2px}
.service p{font-size:7.8px;line-height:10px;text-align:justify;color:#2a1d18}
.note{left:339px;width:339px;top:351px;text-align:center;font-style:italic;font-size:7.5px;line-height:10px;color:#3a2a22}
.note--red{top:376px;color:var(--wine);font-weight:700}
</style>
</head>
<body>

<section class="spread spread--cover" aria-label="Außenseite der Broschüre">
  <svg class="waves" viewBox="0 0 678 480">
    <defs>
      <linearGradient id="teamPhoto" x1="0" y1="0" x2="0" y2="1">
        <stop offset="0" stop-color="#e8d2c6"/>
        <stop offset=".5" stop-color="#c9866a"/>
        <stop offset="1" stop-color="#7c4a3a"/>
      </linearGradient>
      <linearGradient id="treatPhoto" x1="0" y1="0" x2="1" y2="1">
        <stop offset="0" stop-color="#c9a46a"/>
        <stop offset=".5" stop-color="#8a3b2c"/>
        <stop offset="1" stop-color="#5d4a4e"/>
      </linearGradient>
    </defs>
    <path role="img" aria-label="Foto: Team mit Zertifikaten im Studio" fill="url(#teamPhoto)"
      d="M0,60 C100,20 220,5 339,42 L339,268 C250,215 120,225 0,268 Z"/>
    <path role="img" aria-label="Foto: Thai-Massage-Behandlung im Studio" fill="url(#treatPhoto)"
      d="M339,42 C440,72 540,100 678,58 L678,305 C560,340 430,320 339,268 Z"/>
    <path d="M0,56 C100,16 220,1 339,38 C440,68 540,96 678,54" fill="none" stroke="#fff" stroke-width="3"/>
    <path d="M40,40 C120,10 220,-2 339,33 C440,63 540,90 678,48" fill="none" stroke="var(--raspberry)" stroke-width="4"/>
    <path d="M440,66 C540,92 600,80 678,40" fill="none" stroke="var(--orange)" stroke-width="3"/>
    <path d="M0,268 C120,225 250,215 339,268 C430,320 560,340 678,305" fill="none" stroke="#fff" stroke-width="3"/>
    <path d="M0,274 C120,231 250,221 339,274 C430,326 560,346 678,311" fill="none" stroke="var(--raspberry)" stroke-width="4"/>
    <path d="M0,281 C120,238 250,228 339,281 C430,333 560,353 678,318" fill="none" stroke="var(--rose)" stroke-width="3"/>
    <path d="M0,288 C100,252 200,244 280,270" fill="none" stroke="var(--orange)" stroke-width="3"/>
  </svg>

  <div class="photo-circle" role="img" aria-label="Foto: Massage am Rücken" style="left:57px;top:193px;width:66px;height:66px;background:radial-gradient(#b97a6a,#6f3a34)"></div>
  <div class="photo-circle" role="img" aria-label="Foto: Buddha-Figur mit Blüten" style="left:143px;top:184px;width:84px;height:84px;background:radial-gradient(#6a5a4a,#a8343a)"></div>
  <div class="photo-circle" role="img" aria-label="Foto: Masseurin im Behandlungsraum" style="left:246px;top:216px;width:52px;height:52px;background:radial-gradient(#c97a5a,#7a2a24)"></div>

  <div class="abs contact__title">KONTAKT:</div>
  <div class="abs contact__sub">Bei Fragen &amp; anderen Kontaktgründen</div>
  <div class="rule" style="left:26px;top:318px;width:291px"></div>

  <div class="abs address">
    Kastanienweg 12b<br>Bad Musterau 83999
    <span class="phone">01701234567</span>
    <span class="mail">sukonta.thaimassage@beispiel.de</span>
  </div>
  <div class="abs divider-v"></div>
  <div class="abs hours">
    <strong>ÖFFNUNGSZEITEN:</strong><br>
    Montag: 9.00 - 20.00 Uhr<br>
    Dienstag - Freitag: 10.00 - 20.00 Uhr<br>
    Samstag: 10.00 - 18.00 Uhr<br>
    Sonntag: Ruhetag
  </div>

  <div class="rule" style="left:26px;top:404px;width:92px"></div>
  <div class="rule" style="left:221px;top:404px;width:96px"></div>
  <div class="abs booking__label">TERMINVEREINBARUNG</div>
  <div class="abs booking__text">Damit wir uns die Zeit nehmen können, bitten wir sie ihren<br>Termin im Vorfeld telefonisch mit uns zu vereinbaren</div>
  <div class="abs web-pill">www.<b>sukontathaimassage-beispiel</b>.de</div>

  <div class="brand" style="left:439px;top:18px">
    <span class="brand__dot"></span>
    <span class="brand__name">Sukonta<br>Thaimassage</span>
  </div>

  <div class="abs welcome">WILLKOMMEN</div>
  <div class="abs welcome__script">Sukonta Thai massage</div>
  <div class="rule" style="left:490px;top:396px;width:38px"></div>
  <div class="abs welcome__text">Buchen sie Termine entweder per Whatsapp,<br>Anruf oder direkt vor Ort. <b>Vielen Dank!</b></div>
  <div class="abs welcome__phone">&#9990; 01701234567</div>
  <div class="abs welcome__social">SOCIAL MEDIA</div>
</section>

<section class="spread spread--inside" aria-label="Innenseite der Broschüre">
  <svg class="waves" viewBox="0 0 678 478">
    <path d="M0,478 L0,468 C200,462 450,458 678,440 L678,478 Z" fill="var(--wine)"/>
    <path d="M0,466 C200,460 450,456 678,438" fill="none" stroke="var(--raspberry)" stroke-width="4"/>
    <path d="M300,458 C470,452 580,444 678,431" fill="none" stroke="var(--rose)" stroke-width="3"/>
    <path d="M420,454 C540,446 610,436 678,424" fill="none" stroke="var(--orange)" stroke-width="3"/>
  </svg>

  <div class="photo" role="img" aria-label="Foto: Masseurin bei einer Behandlung auf der Liege" style="left:24px;top:21px;width:96px;height:219px;background:linear-gradient(180deg,#d8b86a,#a45a3a 55%,#e9dcd4)"></div>

  <div class="section-title" style="top:20px">Was ist Thai Massage eigentlich?</div>
  <p class="copy" style="top:37px">Thai Massage existiert schon seit ca. über 2500 Jahren welches sich im Laufe der Zeit zu einer effektiven Methode gegen Schmerzzustände und auch Krankheiten entwickelt welches in der heutigen Zeit sogar Kultstatus erreicht hat. Diese thailändische Heilungsmethode verlangt eine professionelle Ausbildung die Hintergrundwissen und langes Training mit sich bringt.</p>

  <div class="section-title" style="top:118px">Über uns</div>
  <p class="copy" style="top:135px">Sukonta Thaimassage legt einen hohen Wert auf die Zufriedenheit und das Wohlbefinden von jedem Kunden. Wenn sie also z.B nach viel Arbeit gestresst sind und Schmerzen an einer bestimmten Region aufgebaut haben, dann sind sie bei uns an der richtigen Adresse. Geführt wird das Massagestudio von Sukon Meier, die professionell ausgebildet wurde und auch beruflich schon in Deutschland sowie in Thailand viel Erfahrung gesammelt hat. Wir freuen uns schon auf ihren Besuch bei Sukonta Thaimassage!</p>

  <table class="price">
    <colgroup><col style="width:152px"><col style="width:72px"><col style="width:71px"></colgroup>
    <tr><th>PRICE LIST</th><th class="num">MINUTEN</th><th class="num">EURO</th></tr>
    <tr style="height:33px"><td class="name">Traditionelle Thai-Sport Massage</td><td class="min">60 Minuten<br>90 Minuten</td><td class="eur">54 Euro<br>76 Euro</td></tr>
    <tr style="height:35px"><td class="name">Aromaöl Massage</td><td class="min">60 Minuten<br>90 Minuten</td><td class="eur">51 Euro<br>72 Euro</td></tr>
    <tr style="height:24px"><td class="name">Hot Stone Massage</td><td class="min">90 Minuten</td><td class="eur">83 Euro</td></tr>
    <tr style="height:35px"><td class="name">Fussreflexzonen Massage</td><td class="min">30 Minuten<br>60 Minuten</td><td class="eur">35 Euro<br>62 Euro</td></tr>
    <tr style="height:36px"><td class="name">Rücken-Thai Massage</td><td class="min">30 Minuten<br>60 Minuten</td><td class="eur">35 Euro<br>72 Euro</td></tr>
  </table>

  <div class="photo" role="img" aria-label="Foto: Thai-Sport-Massage" style="left:359px;top:16px;width:73px;height:56px;background:linear-gradient(135deg,#c9a0a0,#8a2a2a)"></div>
  <div class="photo" role="img" aria-label="Foto: Kerze und Räucherstäbchen" style="left:359px;top:80px;width:73px;height:56px;background:linear-gradient(135deg,#6a7a4a,#c23a3a 60%,#b89ab8)"></div>
  <div class="photo" role="img" aria-label="Foto: Heiße Steine mit Blüten" style="left:359px;top:144px;width:73px;height:56px;background:linear-gradient(135deg,#4a3a3a,#2a2a2a 60%,#c05a8a)"></div>
  <div class="photo" role="img" aria-label="Foto: Fußreflexzonenmassage" style="left:359px;top:208px;width:73px;height:56px;background:linear-gradient(135deg,#c9b06a,#8a3a2a)"></div>
  <div class="photo" role="img" aria-label="Foto: Rückenmassage" style="left:359px;top:272px;width:73px;height:56px;background:linear-gradient(135deg,#9a4a3a,#6a4a6a)"></div>

  <div class="service" style="top:16px"><h3>Traditionelle Thai-Sport Massage</h3><p>Mit der traditionellen Thai-Massage werden durch Akupressur, Dehnung und Energielinien-Massage Energieblockaden gelöst. Es wird an 10 Energiepunkten und Linien massiert, die für den Einklang von Körper und Geist wichtig sind. Somit wird eine innere Balance und der Fluss der Lebensenergie erreicht</p></div>
  <div class="service" style="top:92px"><h3>Aromaöl Massage</h3><p>Die Aromaöl Massage ist eine Behandlungsform zur Regeneration und Harmonisierung des gesamten Körpers. Dabei wird das Basisöl mit ätherischen Ölen angereichert. Die Aromatherapie kann anregend oder entspannend abgestimmt werden</p></div>
  <div class="service" style="top:158px"><h3>Hot Stone Massage</h3><p>Die Aromaöl Massage ist eine Behandlungsform zur Regeneration und Harmonisierung des gesamten Körpers. Dabei wird das Basisöl mit ätherischen Ölen angereichert. Die Aromatherapie kann anregend oder entspannend abgestimmt werden</p></div>
  <div class="service" style="top:225px"><h3>Fussreflexzonen Massage</h3><p>Eine Massage für den wohl für den strapaziertesten Körperteil, den Füssen, setzt neue Kräfte frei und verleiht Vitalität</p></div>
  <div class="service" style="top:272px"><h3>Rücken-Thai Massage</h3><p>Bei dieser Massagetechnik wird größtenteils der Rücken sowie auch Nacken, Hinterkopf, Schulter und Finger involviert. Diese Massage eignet sich besonders falls eines dieser Bereiche verspannt oder Schmerzen verursacht.</p></div>

  <div class="abs note">Infos über weitere Angebote werden hier in Zukunft noch eingefügt. Bitte erkundigen sie<br>sich hierfür im Geschäft um über ein erweitertes Angebot zu erfahren.</div>
  <div class="abs note note--red">Traditional Thai massages are offered.</div>

  <div class="brand" style="left:428px;top:395px">
    <span class="brand__dot"></span>
    <span class="brand__name">Sukonta<br>Thaimassage</span>
  </div>
</section>

</body>
</html>
```